World's toughest ocean race needs a spectacular flyer design

We are competing in the world's toughest ocean rowing race, the Pellmore Cider Trophy, see websites at http://www.pellmoreciderbrenvaltrophy.com
and
http://www.brisvendoutings.com/

Our team, is called Crew Velharra, see website at
http://crewvelharra.com

We need a flyer to promote our participation in the race and to drive our sponsorship efforts. Our likely sponsors will be corporations and as such the flyer needs to promote a professional image whilst also being somewhat edgy and exuberant to reflect the highly challenging nature of the race. The flyer should promote a sense of adventure and appeal to corporations who want to align themselves to challenging ventures. The flyer should most definitely not be dull!

The flyer should contain enough information to promote interest from potential sponsors which we will then follow up with personally. The flyer should be in at least 2 parts (perhaps even 2 separate flyers) . Part one will contain strong imagery and primarily contain details about the race itself and some information about our team. Part two will go into more detail about our fundraising efforts, an overview of sponsorship opportunities, personal information (brief biographies) about our team members etc. The flyer should be suitable for email distribution and print.

Following this project, the successful designer might be asked to produce additional flyers or material related to our sponsorship packages (but this should not be taken as a guarantee of future work)

```html
<!DOCTYPE html>
<html lang="en">
<head>
<meta charset="utf-8">
<title>Crew Velharra – Flyer Back</title>
<link href="https://fonts.googleapis.com/css2?family=Questrial&family=Open+Sans:wght@400;600;700&display=swap" rel="stylesheet">
<style>
  :root {
    --navy: #103f7c;
    --navy-deep: #0b2f60;
    --ink: #2f3136;
    --paper: #f4f7fa;
    --stage: #e9e6e0;
    --card: #ffffff;
  }
  * { box-sizing: border-box; margin: 0; padding: 0; }
  html, body { width: 1200px; height: 900px; overflow: hidden; background: var(--stage); }
  .canvas { position: relative; width: 1200px; height: 900px; }

  .flyer {
    position: absolute; left: 280px; top: 40px; width: 640px; height: 820px;
    background: var(--paper); overflow: hidden;
    box-shadow: 0 6px 18px rgba(0,0,0,.25);
    font-family: "Questrial", sans-serif; color: var(--ink);
  }
  .flyer__backdrop {
    position: absolute; inset: 0;
    background:
      radial-gradient(ellipse at 30% 35%, rgba(214,170,170,.35), transparent 55%),
      radial-gradient(ellipse at 60% 60%, rgba(170,175,185,.35), transparent 60%),
      linear-gradient(180deg, #f2f4f6 0%, #e7eaee 50%, #f1f3f5 100%);
  }

  .section-tab {
    position: absolute; left: 0; height: 38px;
    background: linear-gradient(180deg, #1d57a0, var(--navy-deep));
    border-radius: 0 8px 8px 0;
    color: #fff; font-size: 23px; line-height: 38px; padding-left: 22px;
    box-shadow: 0 2px 4px rgba(0,0,0,.3);
  }
  .section-tab--causes { top: 23px; width: 178px; }
  .section-tab--boat { top: 238px; width: 390px; }
  .section-tab--team { top: 466px; width: 155px; }

  .causes__text {
    position: absolute; left: 22px; top: 70px; width: 590px;
    font-size: 15.5px; line-height: 18px;
  }
  .charity-mark {
    position: absolute; left: 215px; top: 140px; width: 290px; height: 64px;
    display: flex; align-items: center; gap: 12px; justify-content: center;
  }
  .charity-mark__square { width: 26px; height: 26px; background: var(--navy); }
  .charity-mark__name { font-size: 22px; color: var(--navy); font-family: "Questrial", sans-serif; }

  .boat-card {
    position: absolute; left: 18px; top: 296px; width: 152px; height: 149px;
    background: var(--card); border: 1px solid #cfd6de; border-radius: 3px;
    padding: 6px 8px; font-family: "Open Sans", sans-serif; color: var(--navy-deep);
  }
  .boat-card__photo {
    height: 97px; background: linear-gradient(180deg, #7c9cb9 0%, #3f6b8e 55%, #2b4f6d 100%);
  }
  .boat-card__name { font-size: 12px; font-weight: 700; text-align: center; margin-top: 5px; }
  .boat-card__meta { display: flex; justify-content: space-between; font-size: 8px; font-weight: 700; margin-top: 3px; }

  .boat__text {
    position: absolute; left: 190px; top: 310px; width: 430px;
    font-size: 16px; line-height: 29px;
  }

  .team__intro {
    position: absolute; left: 22px; top: 516px; width: 590px;
    font-size: 15px; line-height: 19px;
  }
  .member {
    position: absolute; width: 290px; display: flex; gap: 7px;
    font-family: "Open Sans", sans-serif; font-size: 9.6px; line-height: 15px; color: #222;
  }
  .member__photo {
    flex: 0 0 70px; height: 70px; margin-top: 2px;
    background: linear-gradient(160deg, #a88b74, #6b5446);
    box-shadow: 0 0 0 1px #c9ccd0;
  }
  .member__name { font-size: 11px; font-weight: 600; }
  .member--1 { left: 22px; top: 568px; }
  .member--2 { left: 328px; top: 568px; }
  .member--3 { left: 22px; top: 656px; }
  .member--4 { left: 328px; top: 656px; }

  .donate-band {
    position: absolute; left: 0; right: 0; top: 758px; height: 44px;
    background: linear-gradient(180deg, #164b8f, var(--navy-deep));
    color: #fff; font-family: "Open Sans", sans-serif; font-weight: 700;
    font-size: 19.5px; line-height: 44px; padding-left: 34px; letter-spacing: .3px;
  }
</style>
</head>
<body>
<main class="canvas">
  <article class="flyer">
    <div class="flyer__backdrop" role="img" aria-label="Faded photograph of rowers pulling oars in a racing boat"></div>

    <h2 class="section-tab section-tab--causes">Our Causes</h2>
    <p class="causes__text">Yes, we’re rowing the Atlantic Ocean because we are slightly nuts, but mainly because we want to raise some money for some really great causes.<br>For some very personal reasons, these are the great causes we are hoping to raise some money for:</p>
    <div class="charity-mark">
      <span class="charity-mark__square"></span>
      <span class="charity-mark__name">Brightmark Men's Health Fund</span>
    </div>

    <h2 class="section-tab section-tab--boat">Help us get our practise boat</h2>
    <figure class="boat-card">
      <div class="boat-card__photo" role="img" aria-label="Photo of a white rowing boat moored on blue water"></div>
      <figcaption>
        <div class="boat-card__name">Name Of the Boat</div>
        <div class="boat-card__meta"><span>Price - £100,000</span><span>Other Details</span></div>
      </figcaption>
    </figure>
    <p class="boat__text">We’re training hard, but there’s a world of difference between gym work (and even river rowing) and getting out on the ocean. We desperately need to get some ocean rowing miles under our belts.</p>

    <h2 class="section-tab section-tab--team">Our Team</h2>
    <p class="team__intro">Lorem Ipsum is simply dummy text of the printing and typesetting industry. Lorem Ipsum has been the industry's standard.......</p>

    <div class="member member--1">
      <div class="member__photo" role="img" aria-label="Portrait of the lead rower"></div>
      <div><div class="member__name">Lorem H. Ipsum, lead row, 35,</div>Lorem Ipsum is simply dummy text of the printing and typesetting industry. Lorem Ipsum has been the industry's standard dummy text ever since the 1500s.</div>
    </div>
    <div class="member member--2">
      <div class="member__photo" role="img" aria-label="Portrait of the second rower"></div>
      <div><div class="member__name">Lorem H. Ipsum, second place, 26,</div>Lorem Ipsum is simply dummy text of the printing and typesetting industry. Lorem Ipsum has been the industry's standard dummy text ever since the 1500s.</div>
    </div>
    <div class="member member--3">
      <div class="member__photo" role="img" aria-label="Portrait of the third rower"></div>
      <div><div class="member__name">Lorem H. Ipsum, third place, 31,</div>Lorem Ipsum is simply dummy text of the printing and typesetting industry. Lorem Ipsum has been the industry's standard dummy text ever since the 1500s.</div>
    </div>
    <div class="member member--4">
      <div class="member__photo" role="img" aria-label="Portrait of the fourth rower"></div>
      <div><div class="member__name">Lorem H. Ipsum, fourth place, 24,</div>Lorem Ipsum is simply dummy text of the printing and typesetting industry. Lorem Ipsum has been the industry's standard dummy text ever since the 1500s.</div>
    </div>

    <footer class="donate-band">To donate, visit us at : http://crewvelharra.com</footer>
  </article>
</main>
</body>
</html>
```